Copper Fern Photography

Internet sales of landscape photography
Some background on the name.... I'm originally from Kentucky hence the "Copper" and I now live in California wine country, hence the "Fern." The blue coloring in the name is from the Harlow Falcons and the name "photography" is done in a bourbon lettering font. Hope this helps.
Updates
Please include email as dennis@copperfernphotography.com
Please make website www.copperfernphotography.com and ad QR code if possible.
Industry/Entity Type
Landscape
Contact Information for Business Card
Dennis Marlowe
www.copperfernphoto.com
707-555-0192
Requirements
Must have
- My design logo, all contact info :)
I like the thought of a QR Code along with the written link also.

```html
<!DOCTYPE html>
<html lang="en">
<head>
<meta charset="utf-8">
<title>Copper Fern Photography – Business Card</title>
<link rel="stylesheet" href="https://fonts.googleapis.com/css2?family=Arimo:wght@400;700&display=swap">
<style>
  :root {
    --page: #ffffff;
    --ink-panel: #0e0d15;
    --brand-blue: #045da9;
    --disc-blue: #1c3e72;
    --logo-blue: #1a63b0;
    --contact: #8fb0d3;
  }
  * { margin: 0; padding: 0; box-sizing: border-box; }
  html, body {
    width: 1200px;
    height: 702px;
    overflow: hidden;
    background: var(--page);
  }
  .card {
    position: absolute;
    left: 13px;
    top: 11px;
    width: 1174px;
    height: 681px;
    overflow: hidden;
    font-family: "Arimo", Arial, sans-serif;
  }
  .card__backdrop {
    position: absolute;
    inset: 0;
    width: 100%;
    height: 100%;
  }
  .brand-name {
    position: absolute;
    left: 0;
    width: 1140px;
    top: 278px;
    text-align: center;
    font-size: 50px;
    font-weight: 700;
    letter-spacing: 1px;
    color: var(--logo-blue);
  }
  .contact {
    position: absolute;
    left: 0;
    width: 1140px;
    top: 450px;
    text-align: center;
    color: var(--contact);
    font-size: 33px;
    line-height: 44px;
  }
  .contact__name { font-weight: 700; }
</style>
</head>
<body>
  <main class="card">
    <svg class="card__backdrop" viewBox="0 0 1174 681" aria-hidden="true">
      <defs>
        <clipPath id="right-half">
          <rect x="598" y="0" width="576" height="681"/>
        </clipPath>
      </defs>
      <rect x="0" y="0" width="598" height="681" fill="var(--ink-panel)"/>
      <rect x="598" y="0" width="576" height="681" fill="var(--brand-blue)"/>
      <circle cx="655" cy="331" r="252" fill="var(--disc-blue)" clip-path="url(#right-half)"/>
    </svg>

    <div class="brand-name">Copper Fern Photography</div>

    <div class="contact">
      <p class="contact__name">Dennis Marlowe</p>
      <p class="contact__email">dennis@copperfernphotography.com</p>
      <p class="contact__web">www.copperfernphotography.com</p>
      <p class="contact__phone">707-555-0192</p>
    </div>
  </main>
</body>
</html>
```